My Business is Car Dealership, we sale cars and trucks, I’m looking for a sign design
I need 2 signage
9ā€ by 7ā€ feet.
the other sign is 3" feet high and the width is 12" feet

For further reference about the company , you can check my website
www.harrowbayautosale.com

Industry/Entity Type

Business

Requirements
Must have
• picture of 2018 marlo K240 or 2018 Vantrelle Duskmoor
Nice to have
• the business name Harrow Bay Auto Sale visible from far distance

```html
<!DOCTYPE html>
<html lang="en">
<head>
<meta charset="utf-8">
<title>Harrow Bay Auto Sale – Sign</title>
<link rel="stylesheet" href="https://fonts.googleapis.com/css2?family=Fira+Sans+Condensed:wght@500&family=Roboto:wght@400;700;900&display=swap">
<style>
  :root {
    --ink: #0b0b0d;
    --red: #e31e24;
    --white: #ffffff;
    --band-text: #1a1a1a;
    --night: #151518;
    --car-blue: #1f3a8f;
    --car-deep: #0f1d4f;
    --truck-red: #f0512a;
    --truck-deep: #b8321a;
    --trailer: #e9e9ea;
  }
  * { box-sizing: border-box; margin: 0; padding: 0; }
  html, body { width: 933px; height: 1200px; overflow: hidden; background: var(--ink); }
  .sign {
    position: relative;
    width: 933px;
    height: 1200px;
    overflow: hidden;
    font-family: "Roboto", Arial, sans-serif;
    color: var(--white);
  }
  .scene {
    position: absolute;
    inset: 0 0 93px 0;
    background:
      radial-gradient(ellipse 46% 26% at 50% 42%, rgba(255,230,170,.9) 0%, rgba(243,164,58,.7) 35%, rgba(216,84,31,.35) 65%, rgba(0,0,0,0) 100%),
      linear-gradient(180deg, var(--ink) 0%, var(--night) 30%, #3a2a18 48%, #2a2a2e 72%, #1c1c1f 100%);
  }
  .photo {
    position: absolute;
  }
  .photo-truck {
    left: 566px;
    top: 425px;
    width: 367px;
    height: 415px;
    border-radius: 40px 0 24px 60px;
    background: linear-gradient(100deg, var(--trailer) 0%, var(--trailer) 16%, var(--truck-red) 22%, var(--truck-red) 70%, var(--truck-deep) 100%);
  }
  .photo-car {
    left: 10px;
    top: 692px;
    width: 498px;
    height: 222px;
    border-radius: 120px 160px 40px 30px;
    background: linear-gradient(160deg, #3a5cc0 0%, var(--car-blue) 45%, var(--car-deep) 100%);
  }
  .brand {
    position: absolute;
    top: 56px;
    left: 0;
    width: 100%;
    text-align: center;
  }
  .brand-mark {
    display: block;
    width: 150px;
    height: 150px;
    margin: 0 auto 0;
    border: 7px solid var(--red);
    border-radius: 50%;
  }
  .brand-name {
    margin-top: 0;
    font-family: "Fira Sans Condensed", "Arial Narrow", sans-serif;
    font-weight: 500;
    font-size: 50px;
    line-height: 1;
    color: var(--red);
    letter-spacing: 1px;
  }
  .headline {
    position: absolute;
    left: 0;
    width: 100%;
    text-align: center;
    font-weight: 900;
    line-height: 1;
    paint-order: stroke fill;
  }
  .headline-red {
    top: 268px;
    font-size: 130px;
    color: var(--red);
    -webkit-text-stroke: 6px var(--ink);
  }
  .headline-white {
    font-size: 128px;
    color: var(--white);
    -webkit-text-stroke: 10px var(--ink);
  }
  .line-cars { top: 400px; }
  .line-trucks { top: 530px; }
  .amp { font-size: 76px; vertical-align: -8px; margin-left: 22px; }
  .apply {
    position: absolute;
    left: 88px;
    top: 866px;
    width: 180px;
    text-align: center;
    font-weight: 700;
    font-size: 45px;
    line-height: 1.1;
    color: var(--white);
  }
  .web-pill {
    position: absolute;
    left: 294px;
    top: 882px;
    width: 700px;
    height: 80px;
    background: var(--ink);
    border: 4px solid var(--red);
    border-radius: 40px 0 0 40px;
    display: flex;
    align-items: center;
    padding-left: 24px;
    font-weight: 700;
    font-size: 37px;
    color: var(--white);
  }
  .phone {
    position: absolute;
    left: 0;
    top: 984px;
    width: 100%;
    text-align: center;
    font-weight: 900;
    font-size: 107px;
    line-height: 1;
    letter-spacing: 1px;
    color: var(--white);
    -webkit-text-stroke: 8px var(--red);
    paint-order: stroke fill;
  }
  .promise {
    position: absolute;
    left: 0;
    bottom: 0;
    width: 100%;
    height: 93px;
    background: var(--red);
    display: flex;
    flex-direction: column;
    justify-content: center;
    align-items: center;
    font-size: 27px;
    line-height: 1.22;
    color: var(--band-text);
  }
  .promise b { font-weight: 700; }
</style>
</head>
<body>
  <main class="sign">
    <div class="scene" role="img" aria-label="Night highway on a dark backdrop of halftone diamonds and a warm orange glow"></div>
    <div class="photo photo-truck" role="img" aria-label="Red semi truck with a white trailer speeding along the highway"></div>
    <div class="photo photo-car" role="img" aria-label="Blue sports car with white racing stripes seen from the rear on the highway"></div>

    <header class="brand">
      <span class="brand-mark"></span>
      <p class="brand-name">Harrow Bay Auto Sale</p>
    </header>

    <h1 class="headline headline-red">WE SALE</h1>
    <p class="headline headline-white line-cars">CARS<span class="amp">&amp;</span></p>
    <p class="headline headline-white line-trucks">TRUCKS</p>

    <p class="apply">APPLY<br>ONLINE</p>
    <p class="web-pill">www.harrowbayautosale.com</p>
    <p class="phone">555-014-2760</p>

    <footer class="promise">
      <span>To Provide a <b>Fair</b>, <b>Respectful</b>, and <b>Efficient Service</b></span>
      <span>to all Customers, <b>Everytime, All the Time</b></span>
    </footer>
  </main>
</body>
</html>
```